A paperback book cover entitled: The Quiet Ledger

1. For the front cover of the paperback I need the photo of me walking down the driveway at Wattlebrook Manor as the focal point. The designer will use their discretion where to insert the book title: The Quiet Ledger.
Also the designer will use their discretion where my name Desmond Farrow as the author is placed. Attached is a contemporary photo of me to use if the designer thinks that possible. Both these photos are attached.
2. The back cover page will contain two main written insertions (1) About the Book and (2) About the Author.
The book will be an 8.5x11 inch paperback of some 570 pages published by Pelibrix.
About the book:
This book is about Australian Public Affairs 1957-2020 as perceived and observed by Desmond Farrow. It has a significant but not exclusive Queensland focus concerning History, Commentary, and Anecdotes, plus some things Desmond has been involved with along the way.
Desmond developed unique Transition to Government and Transition to Opposition plans that have all been implemented. Some of those plans are referred to in the book and other Transition plans are appendixes to the book.
Now at 73 years of age, Desmond’s motivation for writing this book is to ensure a wealth of historical scenarios are captured and incorporated into the public record for future generations.

About the author:

Desmond Farrow has been a largely silent and invisible political confidant to Australian Premiers and Prime Ministers.
Desmond worked in the Queensland public sector from 1971-2009 as Chief of Staff to four Queensland State Opposition Leaders for 13 years and then as a Public Sector senior executive.
He subsequently served on the Edith Carrow Trust Board, the Harbourline Reading Institute Board, and consulted to a mining company. He has recorded many Oral History projects for The Calder Archive in Canberra.
Over the last 30+ years, he has been approached countless times for advice relating to Business, Government, Authors, Historians, and people seeking a job. He has never charged a cent for any of his advice, even when not working within Government.
There are two extra photos attached to maybe be on each side at the bottom of the back cover if the designer thinks it is appropriate.
Those in the 4 person photo from the left were all connected with the Tarrington Assembly: former Civic Minister Neil Ostrow, Former Heartland Party Premier Rod Linsey, former Reform Leader Glen Harker, and Desmond Farrow

In the three person photo from the left are: Desmond Farrow, Former PM Bernard Coldwell, and Prime Minister Lionel Parsk.

3. In the spine of the book will be simply (1) The Quiet Ledger and (2) Desmond Farrow

Here’s hoping a good design is created.

```html
<!DOCTYPE html>
<html lang="en">
<head>
<meta charset="utf-8">
<title>The Quiet Ledger — Paperback Cover</title>
<link rel="stylesheet" href="https://fonts.googleapis.com/css2?family=Anton&family=Lato:wght@400;700&display=swap">
<style>
  :root {
    --cover-red: #8b1b0c;
    --title-white: #ffffff;
    --title-outline: #111111;
    --body-text: #ffffff;
    --photo-dark: #3a3a36;
    --photo-mid: #8d8a80;
    --photo-light: #d9d6cc;
    --portrait-bg: #d8d8d8;
    --portrait-suit: #2a3040;
  }
  * { box-sizing: border-box; margin: 0; padding: 0; }
  html, body { width: 1200px; height: 838px; overflow: hidden; }
  body { background: var(--cover-red); font-family: 'Lato', sans-serif; color: var(--body-text); }

  .cover { position: relative; width: 1200px; height: 838px; background: var(--cover-red); }

  /* Shared title treatment */
  .title { font-family: 'Anton', sans-serif; text-transform: uppercase; color: var(--title-white);
           -webkit-text-stroke: 1.5px var(--title-outline); paint-order: stroke fill; line-height: .92; }
  .title .line { display: block; white-space: nowrap; text-align: center; }
  .title .small { -webkit-text-stroke: 0; }
  .photo-letter {
    background: linear-gradient(180deg, var(--photo-light) 0%, var(--photo-mid) 35%, var(--photo-dark) 60%, var(--photo-light) 100%);
    -webkit-background-clip: text; background-clip: text; color: transparent;
  }

  /* Back cover */
  .back { position: absolute; left: 52px; top: 0; width: 460px; }
  .back .title { position: absolute; left: 0; top: 34px; width: 460px; }
  .back .title .small { font-size: 30px; }
  .back .title .big { font-size: 82px; letter-spacing: 1px; }

  .blurb { position: absolute; left: 2px; top: 214px; width: 460px; font-size: 10.2px; line-height: 1.33; }
  .blurb p + p { margin-top: 11px; }

  .photo-pair { position: absolute; top: 363px; left: 0; width: 460px; height: 130px; }
  .photo { position: absolute; top: 0; height: 99px; }
  .photo-group { left: 49px; width: 131px; background: linear-gradient(160deg, #cfcac0, #8f8a80 55%, #4c4a46); }
  .photo-trio { left: 262px; width: 140px; background: linear-gradient(160deg, #d6c9a4, #7c6a4a 55%, #2d2a28); }
  .caption { position: absolute; top: 106px; font-size: 7.3px; line-height: 1.3; text-align: center; }
  .caption-group { left: 0; width: 228px; }
  .caption-trio { left: 228px; width: 236px; }

  .author-heading { position: absolute; left: 0; top: 516px; width: 412px; text-align: center; font-size: 10.4px; letter-spacing: .3px; }
  .author-lead { position: absolute; left: 0; top: 539px; width: 470px; font-size: 8.4px; }
  .portrait { position: absolute; left: 2px; top: 556px; width: 74px; height: 94px; border: 1px solid #e6e6e6;
              background: linear-gradient(180deg, var(--portrait-bg) 0%, #b9b9b9 50%, var(--portrait-suit) 78%); }
  .author-bio { position: absolute; left: 81px; top: 555px; width: 370px; font-size: 8.3px; line-height: 1.3; }
  .author-bio p + p { margin-top: 10px; }

  /* Spine */
  .spine { position: absolute; left: 248px; top: 348px; width: 704px; height: 104px;
           transform: rotate(90deg); transform-origin: 352px 52px;
           display: flex; align-items: center; justify-content: flex-start; }
  .spine-author { font-family: 'Anton', sans-serif; font-size: 41px; line-height: 1; color: var(--title-white);
                  white-space: nowrap; margin-left: 16px; width: 300px; letter-spacing: .5px; }
  .spine .title { margin-left: 14px; }
  .spine .title .line { text-align: left; }
  .spine .title .small { font-size: 28px; }
  .spine .title .big { font-size: 82px; letter-spacing: 1px; }

  /* Front cover */
  .front .title { position: absolute; left: 690px; top: 158px; width: 470px; }
  .front .title .small { font-size: 56px; text-align: left; padding-left: 6px; }
  .front .title .big { font-size: 128px; letter-spacing: 2px; }
  .front-author { position: absolute; left: 696px; top: 684px; width: 440px; text-align: center;
                  font-family: 'Anton', sans-serif; font-size: 52px; line-height: 1; color: var(--title-white); white-space: nowrap; }
</style>
</head>
<body>
<main class="cover">

  <section class="back">
    <h2 class="title">
      <span class="line small">The</span>
      <span class="line big">Qu<span class="photo-letter" role="img" aria-label="Photo of the author walking down the driveway at Wattlebrook Manor">I</span>et</span>
      <span class="line big">Ledger</span>
    </h2>

    <div class="blurb">
      <p>This book is about Australian Public Affairs 1957-2020 as perceived and observed by Desmond Farrow.</p>
      <p>It has a significant but not exclusive Queensland focus concerning History, Commentary, and Anecdotes, plus some things Desmond has been involved with along the way.<br>
      Desmond developed unique Transition to Government and Transition to Opposition plans that have all been implemented.<br>
      Some of those plans are referred to in the book and other Transition plans are appendixes to the book.</p>
      <p>Now at 73 years of age, Desmond’s motivation for writing this book is to ensure a wealth of historical scenarios are captured and incorporated into the public record for future generations.</p>
    </div>

    <div class="photo-pair">
      <div class="photo photo-group" role="img" aria-label="Photo of four men standing together in a dining room"></div>
      <div class="photo photo-trio" role="img" aria-label="Signed photo of three men, one seated, in a panelled room"></div>
      <p class="caption caption-group">Civic Minister Neil Ostrow, Heartland Party Premier Rod Linsey,<br>Reform Leader Glen Harker, and Desmond Farrow</p>
      <p class="caption caption-trio">Desmond Farrow,<br>Former PM Bernard Coldwell, and Prime Minister Lionel Parsk.</p>
    </div>

    <h3 class="author-heading">ABOUT THE AUTHOR</h3>
    <p class="author-lead">Desmond Farrow has been a largely silent and invisible political confidant to Australian Premiers and Prime Ministers.</p>
    <div class="portrait" role="img" aria-label="Contemporary portrait photo of the author"></div>
    <div class="author-bio">
      <p>Desmond worked in the Queensland public sector from 1971-2009 as Chief of Staff to four Queensland State Opposition Leaders for 13 years and then as a Public Sector senior executive. He subsequently served on the Edith Carrow Trust Board, the Harbourline Reading Institute Board, and consulted to a mining company. He has recorded many Oral History projects for The Calder Archive in Canberra.</p>
      <p>Over the last 30+ years, he has been approached countless times for advice relating to Business, Government, Authors, Historians, and people seeking a job.<br>
      He has never charged a cent for any of his advice, even when not working within Government.</p>
    </div>
  </section>

  <section class="spine">
    <span class="spine-author">DESMOND FARROW</span>
    <h2 class="title">
      <span class="line small">The Quiet</span>
      <span class="line big">Ledger</span>
    </h2>
  </section>

  <section class="front">
    <h1 class="title">
      <span class="line small">The</span>
      <span class="line big">Qu<span class="photo-letter" role="img" aria-label="Photo of the author walking down the driveway at Wattlebrook Manor">I</span>et</span>
      <span class="line big">Ledger</span>
    </h1>
    <p class="front-author">DESMOND FARROW</p>
  </section>

</main>
</body>
</html>
```